Health care technology software systems

We have a solid logo. We have company colors that will need to be used as well. We just need a great business card design. We sell to health plans but want to be modern
Updates

Need extra days to review

Target Market(s)

Health technology sector selling into Health Plans

Industry/Entity Type

Health Care Technology

Contact Information for Business Card

Name, title, address, phone number, email

Requirements
Must have
• Use of Kembrata corporate colors - Uploaded w/ our logos

```html
<!DOCTYPE html>
<html lang="en">
<head>
<meta charset="utf-8">
<title>Kembrata Business Card</title>
<link href="https://fonts.googleapis.com/css2?family=Source+Sans+3:wght@300;400;600&display=swap" rel="stylesheet">
<style>
  :root {
    --backdrop: #e6e6e6;
    --card-dark: #2e302f;
    --card-light: #f4f4f4;
    --brand-blue: #1a9ad6;
    --brand-navy: #3a5bb0;
    --brand-green: #7ab833;
    --ink: #333333;
    --white: #ffffff;
  }
  * { margin: 0; padding: 0; box-sizing: border-box; }
  html, body {
    width: 1200px; height: 960px; overflow: hidden;
    background: var(--backdrop);
    font-family: "Source Sans 3", sans-serif;
  }
  .stage { position: relative; width: 1200px; height: 960px; }

  .card {
    position: absolute; left: 307px; width: 596px; height: 341px;
    border-radius: 22px; overflow: hidden;
  }
  .card--front { top: 114px; background: var(--card-dark); }
  .card--back  { top: 507px; background: var(--card-light); }

  .front-texture {
    position: absolute; inset: 0;
    background: linear-gradient(90deg, #6f7170 0%, #4a4c4b 40%, #1d1e1d 70%, #0c0c0c 100%);
  }

  .wordmark {
    position: absolute; display: flex; align-items: center;
    font-weight: 300; letter-spacing: 1px; line-height: 1;
  }
  .wordmark__dot { border-radius: 50%; background: var(--brand-blue); flex: none; }
  .wordmark--front { left: 268px; top: 203px; color: var(--white); font-size: 56px; }
  .wordmark--front .wordmark__dot { width: 58px; height: 58px; margin-right: 22px; }
  .wordmark--back { left: 46px; top: 143px; color: var(--ink); font-size: 48px; }
  .wordmark--back .wordmark__dot { width: 48px; height: 48px; margin-right: 18px; }

  .back-glow {
    position: absolute; left: 34px; top: 30px; width: 270px; height: 280px;
    background: radial-gradient(ellipse at center, rgba(225,232,238,0.9) 0%, rgba(226,236,222,0.55) 55%, rgba(244,244,244,0) 75%);
  }

  .contact { position: absolute; left: 356px; top: 76px; color: var(--ink); }
  .contact__name { color: var(--brand-blue); font-weight: 600; font-size: 19px; line-height: 24px; }
  .contact__title { font-size: 15px; line-height: 20px; }
  .contact__rule { width: 29px; height: 3px; background: var(--brand-navy); margin: 16px 0 14px; }
  .contact__address { font-size: 15px; line-height: 20px; margin-bottom: 8px; }
  .contact__line { display: flex; align-items: center; font-size: 15px; line-height: 20px; }
  .contact__line svg { width: 13px; height: 13px; margin-right: 6px; flex: none; }
</style>
</head>
<body>
<main class="stage">
  <section class="card card--front">
    <div class="front-texture" role="img" aria-label="Repeating brand pattern fading from grey to black"></div>
    <div class="wordmark wordmark--front"><span class="wordmark__dot"></span>kembrata</div>
  </section>

  <section class="card card--back">
    <div class="back-glow" role="img" aria-label="Faint large brand decoration in soft blue and green"></div>
    <div class="wordmark wordmark--back"><span class="wordmark__dot"></span>kembrata</div>

    <div class="contact">
      <p class="contact__name">Daniel Hartley</p>
      <p class="contact__title">President</p>
      <div class="contact__rule"></div>
      <p class="contact__address">2400 NW ALDER ST 210<br>Salem, Oregon 97301</p>
      <p class="contact__line">
        <svg viewBox="0 0 16 16" aria-hidden="true"><path d="M3 1.5l3 .5 1 3.5-2 1.5a9 9 0 0 0 4 4l1.5-2 3.5 1 .5 3-2 1.5C7 14 2 9 1.5 3.5z" fill="var(--brand-green)"/></svg>
        (555) 318-4027
      </p>
      <p class="contact__line">
        <svg viewBox="0 0 16 16" aria-hidden="true"><rect x="1" y="3" width="14" height="10" fill="none" stroke="var(--brand-green)" stroke-width="1.6"/><path d="M1 3l7 6 7-6" fill="none" stroke="var(--brand-green)" stroke-width="1.6"/></svg>
        daniel@kembrata.com
      </p>
      <p class="contact__line">
        <svg viewBox="0 0 16 16" aria-hidden="true"><g fill="none" stroke="var(--brand-green)" stroke-width="1.4"><circle cx="8" cy="8" r="6.5"/><ellipse cx="8" cy="8" rx="3" ry="6.5"/><path d="M1.5 8h13"/></g></svg>
        www.kembrata.com
      </p>
    </div>
  </section>
</main>
</body>
</html>
```